Banner Pop Up Opt In Form REDESIGNS - SLEEK BLACK LOOK

Please redesign banners attached.

I am looking for a very sleek look....I do not like this collage of images on these current designs. Please keep all content same but use images that pop.

I have an acccount at www.pixmorrow-example.com or you can use your own images.

I like black background for somereason because it looks very sleek....but these designs should pop , build trust and credibility and have easy opt in form....SLEEK AND MODERN LOOK is what im looking for....

Target Market(s)

Consumers on websites

Requirements
Must have
• Please redesign banners attached.

Nice to have

Should not have

```html
<!DOCTYPE html>
<html lang="en">
<head>
<meta charset="UTF-8">
<title>Hotel Savings Card Opt-In Banners</title>
<link rel="stylesheet" href="https://fonts.googleapis.com/css2?family=Playfair+Display:wght@600;700&family=Montserrat:wght@400;500;600;700&display=swap">
<style>
  :root {
    --page-black: #000000;
    --panel-black: #0d0d0d;
    --accent-orange: #f2a14a;
    --accent-orange-deep: #e8902f;
    --ink-dark: #1c1410;
    --text-white: #ffffff;
    --text-soft: #d9d9d9;
    --form-veil: rgba(255, 255, 255, 0.82);
    --line-grey: #8a8a8a;
  }
  * { box-sizing: border-box; margin: 0; padding: 0; }
  html, body {
    width: 1200px; height: 2400px; overflow: hidden;
    background: var(--page-black);
    font-family: "Montserrat", Arial, sans-serif;
  }
  .canvas { position: relative; width: 1200px; height: 2400px; background: var(--page-black); }

  .banner { position: absolute; left: 120px; width: 960px; overflow: hidden; }
  .banner--offer { top: 140px; height: 960px; }
  .banner--contest { top: 1280px; height: 980px; background: var(--panel-black); }

  .photo { position: absolute; left: 0; top: 0; width: 100%; }
  .photo--pool {
    height: 100%;
    background:
      linear-gradient(180deg, rgba(0,0,0,0.55) 0%, rgba(0,0,0,0.25) 35%, rgba(0,0,0,0) 55%),
      linear-gradient(180deg, #2f3a24 0%, #4d5a3a 30%, #7d8a6d 48%, #6fa9c4 62%, #3f8db5 78%, #9fc3d3 100%);
  }
  .photo--bedroom {
    height: 560px;
    background:
      radial-gradient(ellipse at 50% 60%, rgba(200,170,130,0.35) 0%, rgba(0,0,0,0) 55%),
      linear-gradient(180deg, #1a1a1c 0%, #2b2a2b 45%, #4a3c30 75%, #2a2019 100%);
  }

  .headline {
    font-family: "Playfair Display", Georgia, serif;
    font-weight: 700; color: var(--accent-orange);
    letter-spacing: 2px; text-transform: uppercase;
  }
  .banner--offer .headline {
    position: absolute; top: 50px; width: 100%; text-align: center; font-size: 58px;
  }
  .lead {
    color: var(--text-white); font-weight: 500; text-transform: uppercase; letter-spacing: 2px;
  }
  .banner--offer .lead {
    position: absolute; top: 138px; width: 100%; text-align: center;
    font-size: 26px; line-height: 40px;
  }

  .ribbon {
    position: absolute; background: var(--accent-orange);
    color: var(--ink-dark); font-weight: 700; text-transform: uppercase;
    letter-spacing: 1px; text-align: center; display: flex; flex-direction: column; justify-content: center;
  }
  .banner--offer .ribbon {
    top: 216px; left: 260px; width: 440px; height: 80px;
    font-size: 27px; line-height: 32px;
    clip-path: polygon(0 0, 100% 0, 95% 50%, 100% 100%, 0 100%, 5% 50%);
  }

  .optin-panel {
    position: absolute; left: 0; top: 756px; width: 100%; height: 164px;
    background: var(--form-veil);
    display: grid; grid-template-columns: 1fr 1fr; column-gap: 80px; row-gap: 22px;
    padding: 28px 40px 0;
  }
  .field {
    border-bottom: 2px solid var(--line-grey);
    height: 44px; display: flex; align-items: center; justify-content: center;
    color: #555; font-size: 22px; letter-spacing: 3px; text-transform: uppercase;
  }
  .submit {
    height: 48px; display: flex; align-items: center; justify-content: center;
    font-weight: 700; font-size: 24px; letter-spacing: 4px; text-transform: uppercase;
  }
  .optin-panel .submit { background: var(--ink-dark); color: var(--text-white); }

  .notice {
    font-size: 15px; text-transform: uppercase; letter-spacing: 1px; text-align: center;
  }
  .banner--offer .notice {
    position: absolute; left: 0; top: 920px; width: 100%; height: 40px;
    background: var(--accent-orange-deep); color: var(--ink-dark);
    display: flex; align-items: center; justify-content: center; font-weight: 500;
  }

  .banner--contest .headline {
    position: absolute; left: 32px; top: 618px; font-size: 62px;
  }
  .banner--contest .lead {
    position: absolute; left: 32px; top: 700px; font-size: 24px; line-height: 40px; color: var(--text-soft);
  }
  .banner--contest .ribbon {
    top: 808px; left: 20px; width: 330px; height: 72px;
    font-size: 24px; line-height: 30px; text-align: left; padding-left: 22px;
    clip-path: polygon(0 0, 86% 0, 100% 100%, 0 100%);
  }
  .entry-form {
    position: absolute; left: 600px; top: 600px; width: 340px;
    display: flex; flex-direction: column; gap: 24px;
  }
  .entry-form .field { color: var(--text-soft); border-bottom-color: var(--text-soft); height: 46px; }
  .entry-form .submit { background: var(--accent-orange); color: var(--ink-dark); margin-top: 4px; }
  .banner--contest .notice {
    position: absolute; left: 0; top: 940px; width: 100%; color: var(--text-soft);
  }
</style>
</head>
<body>
<main class="canvas">

  <section class="banner banner--offer">
    <div class="photo photo--pool" role="img" aria-label="Photo of a woman in a sun hat relaxing on a lounge chair by a resort pool among palm trees"></div>
    <h1 class="headline">Want a great offer?</h1>
    <p class="lead">Subscribe to our newsletter and<br>receive a complimentary</p>
    <div class="ribbon"><span>$500 Hotel</span><span>Savings Cards</span></div>
    <form class="optin-panel">
      <div class="field">Name</div>
      <div class="field">Email</div>
      <div class="field">Phone</div>
      <div class="submit">Submit</div>
    </form>
    <p class="notice">We will send an email and a text message with the offer and instructions on how to redeem</p>
  </section>

  <section class="banner banner--contest">
    <div class="photo photo--bedroom" role="img" aria-label="Photo of a modern dark hotel bedroom with a bed, bedside lamps and a yellow armchair"></div>
    <h2 class="headline">Enter to win</h2>
    <p class="lead">Subscribe to our newsletter<br>to enter to win a</p>
    <div class="ribbon"><span>$500 Hotel</span><span>Savings Cards</span></div>
    <form class="entry-form">
      <div class="field">Name</div>
      <div class="field">Email</div>
      <div class="field">Phone</div>
      <div class="submit">Submit</div>
    </form>
    <p class="notice">We will send an email and a text message with the offer and instructions on how to redeem</p>
  </section>

</main>
</body>
</html>
```